Fenwick Chillform Brochure

I would like a simple brochure of very high quality that exudes a prestigious image. The business I run offers a solution for permanent fat loss but is non-invasive and a fraction of the cost of liposuction. I am a sole trader and run a local business from my home. The technology is called Cryolypolysis. It is extremely popular in the US and is breaking in to the UK market. It is virtually pain free, non-invasive, no downtime, and helps people reduce areas with localized fat that do not respond to diet and exercise Ideally, I would like a brochure that folds 3 ways and of very high quality. I offer bespoke services and packages for body scutlping (mulitple treatments to help accentuate mulscle definition). I also have flexible hours for people requiring appointments evenings and weekends. My branding is visible on my website: www.fenwickchillform.example

Target Market(s)

The typical buyer will be someone who is either slightly overweight OR someone who is average and just can't shirt weight in specific areas. It s also useful for people who exercise and want help exposing muscle definition.

Industry/Entity Type

Business

Colors
3176b5
85acd3
33a6d7
ffffff

Requirements
Must have
• I need the following included:
1. The before and after pics
2. The treatable Areas
3. Don't list the prices, but say "Prices start at £400"
4. Do not include Christmas Special as this is temporary
Should not have
• Full price list

```html
<!DOCTYPE html>
<html lang="en">
<head>
<meta charset="utf-8">
<title>Fenwick Chillform Brochure</title>
<link href="https://fonts.googleapis.com/css2?family=Lato:wght@400;700;900&display=swap" rel="stylesheet">
<style>
  :root {
    --page-bg: #d9dde1;
    --sheet-top: #eef4f9;
    --sheet-bottom: #d6e7f3;
    --navy: #1f67a6;
    --brand-blue: #3176b5;
    --soft-blue: #85acd3;
    --sky: #33a6d7;
    --panel-light: #82d4f7;
    --panel-mid: #5cc4f0;
    --badge: #4cc0ef;
    --ink: #333a40;
    --ink-dark: #0f2c47;
    --white: #ffffff;
  }
  * { box-sizing: border-box; margin: 0; padding: 0; }
  html, body {
    width: 1200px; height: 900px; overflow: hidden;
    background: var(--page-bg);
    font-family: "Lato", Arial, sans-serif;
  }
  .brochure {
    position: absolute; left: 30px; top: 44px;
    width: 1140px; height: 812px; overflow: hidden;
    background: linear-gradient(180deg, var(--sheet-top), var(--sheet-bottom));
    box-shadow: 0 4px 18px rgba(0,0,0,0.18);
  }
  .brochure-art { position: absolute; inset: 0; width: 1140px; height: 812px; }
  .testimonial {
    position: absolute; left: 44px; top: 80px; width: 360px;
    font-weight: 700; font-size: 21px; line-height: 1.26; color: var(--ink);
  }
  .price-badge {
    position: absolute; left: 188px; top: 597px; width: 192px; height: 192px;
    display: flex; flex-direction: column; align-items: center; justify-content: center;
    text-align: center; line-height: 1;
  }
  .price-badge .lead { font-weight: 900; font-size: 31px; color: var(--ink-dark); }
  .price-badge .amount { font-weight: 900; font-size: 48px; color: var(--white); margin-top: 4px; }
  .contact {
    position: absolute; left: 433px; top: 578px; list-style: none;
    font-weight: 700; font-size: 16px; color: var(--ink-dark); line-height: 1.22;
  }
  .contact li { display: flex; gap: 12px; align-items: flex-start; margin-bottom: 12px; }
  .contact svg { flex: none; width: 14px; height: 14px; margin-top: 2px; }
  .web-button {
    position: absolute; top: 744px; height: 68px;
    background: var(--navy); border-radius: 16px 16px 0 0;
    display: flex; align-items: center; justify-content: center;
    color: var(--white); font-weight: 700; font-size: 15.5px; letter-spacing: 0.6px;
  }
  .web-button.left { left: 428px; width: 312px; }
  .web-button.right { left: 800px; width: 310px; }
  .brand-name {
    position: absolute; left: 780px; top: 650px; width: 350px; text-align: center;
    font-weight: 700; font-size: 38px; color: var(--brand-blue); letter-spacing: 0.3px;
  }
</style>
</head>
<body>
<main class="brochure">
  <svg class="brochure-art" viewBox="0 0 1140 812" aria-hidden="false">
    <defs>
      <linearGradient id="iceTone" x1="0" y1="0" x2="0" y2="1">
        <stop offset="0" stop-color="#dfeaf2"/>
        <stop offset="1" stop-color="#9fb6c8"/>
      </linearGradient>
      <linearGradient id="skinTone" x1="0" y1="0" x2="1" y2="1">
        <stop offset="0" stop-color="#f4f1ee"/>
        <stop offset="0.5" stop-color="#e2b8a0"/>
        <stop offset="1" stop-color="#f0ebe8"/>
      </linearGradient>
      <linearGradient id="panelTone" x1="0" y1="0" x2="0" y2="1">
        <stop offset="0" stop-color="var(--panel-light)"/>
        <stop offset="1" stop-color="var(--panel-mid)"/>
      </linearGradient>
    </defs>

    <rect class="ice-photo" x="500" y="0" width="640" height="470" fill="url(#iceTone)" opacity="0.85"
          role="img" aria-label="Photo of stacked ice cubes melting on a reflective surface"/>

    <path class="model-photo" d="M0,360 C220,300 520,330 760,460 L760,812 L0,812 Z" fill="url(#skinTone)"
          role="img" aria-label="Photo of a woman measuring her thigh with a yellow tape measure"/>

    <path class="wave-dark" d="M0,205 C260,150 520,250 720,360 C880,450 1010,410 1140,300
             L1140,455 C1010,500 880,500 720,440 C520,360 260,330 0,470 Z" fill="var(--navy)"/>
    <path class="wave-stripe" d="M0,262 C260,215 520,300 720,395 C880,470 1010,445 1140,370
             L1140,385 C1010,462 880,484 720,410 C520,318 260,240 0,285 Z" fill="#6ec8f2"/>

    <path class="wave-white" d="M170,812 C300,580 520,470 760,452 C930,440 1040,440 1140,430 L1140,812 Z" fill="var(--white)"/>
    <path class="wave-sky" d="M200,812 C320,600 530,498 760,482 C930,470 1040,480 1140,474 L1140,812 Z" fill="var(--sky)" opacity="0.55"/>
    <path class="info-panel" d="M255,812 C360,640 540,530 760,508 C930,492 1040,505 1140,500 L1140,812 Z" fill="url(#panelTone)"/>
    <line class="panel-divider" x1="764" y1="510" x2="764" y2="812" stroke="var(--white)" stroke-opacity="0.5" stroke-width="2"/>

    <circle class="badge-disc" cx="284" cy="693" r="96" fill="var(--badge)"/>
    <circle class="badge-ring" cx="284" cy="693" r="84" fill="none" stroke="var(--white)" stroke-width="3" stroke-dasharray="7 5"/>
  </svg>

  <p class="testimonial">“After considering liposuction for years, I finally got the results I wanted with Chillform.”</p>

  <div class="price-badge">
    <span class="lead">Prices<br>start at</span>
    <span class="amount">£400</span>
  </div>

  <ul class="contact">
    <li>
      <svg viewBox="0 0 14 14"><circle cx="7" cy="7" r="7" fill="#fff"/><path d="M3.5,7.3 L7,4 L10.5,7.3 M4.7,6.5 V10 H9.3 V6.5" fill="none" stroke="#5cc4f0" stroke-width="1.4"/></svg>
      <span>9 Larch Close<br>Hollin Green<br>Westmorland<br>HG4 7TQ</span>
    </li>
    <li>
      <svg viewBox="0 0 14 14"><circle cx="7" cy="7" r="7" fill="#fff"/><path d="M4.5,3.8 L6,5.6 L5.2,6.6 C5.8,7.8 6.4,8.4 7.5,8.9 L8.4,8.1 L10.2,9.6 L9.3,10.6 C6.6,10.4 3.8,7.6 3.5,4.8 Z" fill="#5cc4f0"/></svg>
      <span>07700 900 214</span>
    </li>
    <li>
      <svg viewBox="0 0 14 14"><circle cx="7" cy="7" r="7" fill="#fff"/><rect x="3.6" y="4.6" width="6.8" height="4.8" fill="none" stroke="#5cc4f0" stroke-width="1.2"/><path d="M3.6,4.6 L7,7.4 L10.4,4.6" fill="none" stroke="#5cc4f0" stroke-width="1.2"/></svg>
      <span>info@fenwickchillform.example</span>
    </li>
  </ul>

  <div class="brand-name">Fenwick Chillform</div>

  <div class="web-button left">www.fenwickchillform.example</div>
  <div class="web-button right">www.fenwickchillform.example</div>
</main>
</body>
</html>
```